New Plumbing Company

We are looking for a smart and creative business card design for our new plumbing company. We are looking for creativity and originality in our business cards.

Industry/Entity Type

Plumbing

Contact Information for Business Card

Crestline Plumbing
Peter Halvane
Managing Director
Telephone Number : 0481529604
Email : service@crestlineplumbing.com.au
Website : www.crestlineplumbing.com.au
Lic. 508264K

Colors
0692cd
33a6d7
000000

Requirements
Must have
• I want the business card to be designed on a black background using the blue tones i have selected as seen in the company logo.

```html
<!DOCTYPE html>
<html lang="en">
<head>
<meta charset="utf-8">
<title>Crestline Plumbing – Business Card</title>
<link href="https://fonts.googleapis.com/css2?family=Open+Sans:wght@400;600;700&display=swap" rel="stylesheet">
<style>
  :root {
    --backdrop: #5b4130;
    --card: #2a2a2b;
    --brand-blue: #0692cd;
    --accent-blue: #33a6d7;
    --text-light: #f2f2f2;
    --emboss: #1d1d1e;
    --emboss-edge: #3a3a3b;
  }
  * { margin: 0; padding: 0; box-sizing: border-box; }
  html, body {
    width: 1200px; height: 1000px; overflow: hidden;
    background: var(--backdrop);
    font-family: "Open Sans", Arial, sans-serif;
  }
  .card {
    position: absolute;
    left: 265px; width: 665px;
    background: var(--card);
    box-shadow: 0 6px 18px rgba(0,0,0,0.35);
  }
  .card--front { top: 73px; height: 397px; border-radius: 60px 8px 60px 8px; }
  .card--back  { top: 533px; height: 432px; border-radius: 8px 60px 8px 60px; }

  .brand { position: absolute; display: flex; align-items: center; gap: 16px; }
  .brand__dot {
    width: 82px; height: 82px; border-radius: 50%;
    border: 4px solid var(--brand-blue);
    flex: none;
  }
  .brand__name { font-weight: 600; font-size: 34px; color: var(--brand-blue); white-space: nowrap; }
  .card--front .brand { left: 300px; top: 115px; position: fixed; }

  .person { position: absolute; right: 32px; top: 194px; text-align: right; }
  .person__name { font-weight: 700; font-size: 21px; color: var(--brand-blue); letter-spacing: 0.3px; line-height: 30px; }
  .person__role { font-size: 17px; color: var(--text-light); line-height: 26px; }

  .licence { position: absolute; left: 33px; top: 255px; font-size: 16px; color: var(--text-light); }

  .contacts { position: absolute; left: 33px; top: 292px; list-style: none; }
  .contacts li { display: flex; align-items: center; height: 26px; font-size: 17px; color: var(--text-light); }
  .contacts svg { width: 14px; height: 14px; margin-right: 12px; fill: var(--accent-blue); flex: none; }

  .card--back .brand { left: 50%; top: 50%; transform: translate(-50%, -50%); }
  .card--back .brand__dot { width: 96px; height: 96px; border-color: var(--emboss); }
  .card--back .brand__name { font-size: 44px; color: var(--emboss); text-shadow: none; }
</style>
</head>
<body>
  <section class="card card--front">
    <div class="brand">
      <span class="brand__dot"></span>
      <span class="brand__name">Crestline Plumbing</span>
    </div>
    <div class="person">
      <p class="person__name">PETER HALVANE</p>
      <p class="person__role">Managing Director</p>
    </div>
    <p class="licence">Lic. 508264K</p>
    <ul class="contacts">
      <li>
        <svg viewBox="0 0 16 16" aria-hidden="true"><path d="M2 5c0-2 2-3 6-3s6 1 6 3v1h-3V5H5v1H2zM4 7h8l2 6H2z"/></svg>
        0481529604
      </li>
      <li>
        <svg viewBox="0 0 16 16" aria-hidden="true"><path d="M1 3h14v10H1zM2 4v1l6 4 6-4V4z"/></svg>
        service@crestlineplumbing.com.au
      </li>
      <li>
        <svg viewBox="0 0 16 16" aria-hidden="true"><path d="M8 1a7 7 0 1 0 0 14A7 7 0 0 0 8 1zm0 2a5 5 0 0 1 4.6 3H10c-.3-1-.9-2-2-3zm-2 0C5 4 4.4 5 4.1 6H3.4A5 5 0 0 1 6 3zM3 8h1c0 1 .2 2 .5 3h-1A5 5 0 0 1 3 8zm3 0h4c0 1-.3 2-.6 3H6.6C6.3 10 6 9 6 8zm6 0h1a5 5 0 0 1-.5 3h-1c.3-1 .5-2 .5-3z"/></svg>
        www.crestlineplumbing.com.au
      </li>
    </ul>
  </section>

  <section class="card card--back">
    <div class="brand">
      <span class="brand__dot"></span>
      <span class="brand__name">Crestline Plumbing</span>
    </div>
  </section>
</body>
</html>
```